International IT and cyber security consulting company is looking to establish a web presence.

Harwell Mariner Advisory LLC provides IT, cyber security, risk, project management and data analytics consulting services worldwide. Our clients are both government and corporate. We are looking to establish a basic web presence with about 6 pages (Home, About Harwell, Our Experts, News and Events, Careers, Contact Us). The designs should set the look and feel of the site for further build out down the line. The final design should be straightforward and simple and allow us to convey information about our consulting services clearly.

Target Market(s)

Government and corporate clients or potential clients, job seekers.

Industry/Entity Type

Consulting

Contact Information for Business Card

The cards will have english on the front and arabic on the back. The design should be the same on both sides.

Coding

Number of Pages Required

Font styles to use
Serif
Sans Serif

Requirements
Must have
• The pages should be simple but visually appealing with a picture or graphic that is appropriate to the company or services we offer. Our name and logo should be branded throughout the design. While we are mostly an IT company we also have a line of business where we organize speaking events for VIPs so the website shouldn't overly emphasize our IT work.
Should not have
• No cartoons or drawings. The site should not have overly flashy or loud colors. We cater to a conservative set of clients so the site should match what they expect to see in an international consultancy's website. There should not be an overuse of the color orange because it can be hard on the eyes if it is used too much on the page. Also, please do not use graphics or pictures that use locks, keys, castles, shields etc since these are too commonly used in the cyber security industry.

```html
<!DOCTYPE html>
<html lang="en">
<head>
<meta charset="utf-8">
<title>Harwell Mariner Advisory LLC</title>
<link href="https://fonts.googleapis.com/css2?family=Poppins:wght@400;500;600;700&display=swap" rel="stylesheet">
<style>
:root{
  --orange:#f37021;
  --ink:#151515;
  --dark:#161616;
  --text:#2a2a2a;
  --muted:#6d6d6d;
  --soft:#f3f3f3;
  --line:#d0d0d0;
  --white:#ffffff;
}
html,body{margin:0;padding:0;overflow:hidden;background:var(--white);}
body{width:1200px;height:4131px;font-family:'Poppins',sans-serif;color:var(--text);}
.page{position:relative;width:1200px;height:4131px;overflow:hidden;background:var(--white);}
.abs{position:absolute;}
.bg-svg{position:absolute;left:0;display:block;}

/* header */
.brand{position:absolute;left:88px;top:26px;display:flex;align-items:center;gap:10px;}
.brand-name{font-family:'Poppins',sans-serif;font-weight:500;color:var(--orange);font-size:13px;line-height:15px;letter-spacing:1.5px;text-transform:uppercase;}
.brand-mark{width:12px;height:12px;background:var(--orange);}
.nav{position:absolute;right:90px;top:42px;display:flex;gap:32px;font-size:12.5px;font-weight:500;letter-spacing:.3px;color:var(--ink);text-transform:uppercase;}

/* shared */
.eyebrow{position:absolute;display:flex;align-items:center;gap:12px;font-size:12px;font-weight:600;letter-spacing:.6px;color:#8a8a8a;text-transform:uppercase;}
.eyebrow::before{content:"";display:block;width:78px;height:1px;background:#9a9a9a;}
.btn{position:absolute;display:flex;align-items:center;justify-content:center;background:var(--orange);color:var(--white);font-size:13px;font-weight:600;letter-spacing:.6px;text-transform:uppercase;}
.photo{position:absolute;}

/* hero */
.hero-title{position:absolute;left:68px;top:222px;margin:0;font-size:58px;line-height:63px;font-weight:700;color:var(--ink);}
.hero-text{position:absolute;left:70px;top:444px;width:430px;margin:0;font-size:15px;line-height:24px;color:#333;}

/* about */
.about-title{position:absolute;left:723px;top:962px;margin:0;font-size:37px;line-height:42px;font-weight:600;color:var(--white);}
.about-text{position:absolute;left:723px;width:420px;margin:0;font-size:13.5px;line-height:22px;color:#c9c9c9;}

/* services */
.service{position:absolute;top:1512px;width:300px;text-align:center;}
.service svg{display:block;margin:0 auto;}
.service h3{margin:14px 0 8px;font-size:17px;font-weight:600;color:var(--ink);}
.service p{margin:0 auto;width:220px;font-size:13px;line-height:22px;color:var(--muted);}

/* careers */
.careers-title{position:absolute;left:87px;top:1938px;width:500px;margin:0;font-size:38px;line-height:43px;font-weight:700;color:var(--ink);}
.careers-text{position:absolute;left:91px;top:2088px;width:460px;margin:0;font-size:13.5px;line-height:22px;color:#444;}

/* team */
.member{position:absolute;top:2448px;width:266px;height:415px;background:var(--white);}
.member .portrait{width:266px;height:300px;}
.member h4{margin:24px 0 0 34px;font-size:17px;font-weight:600;color:var(--ink);white-space:nowrap;}
.member span{display:block;margin:4px 0 0 34px;font-size:13px;color:#9a9a9a;}
.member.edge h4,.member.edge span{margin-left:108px;}
.member.active{box-shadow:0 10px 30px rgba(0,0,0,.12);}
.view-link{position:absolute;left:34px;top:377px;font-size:19px;font-weight:500;color:var(--ink);}
.view-link::after{content:"";position:absolute;left:0;bottom:-4px;width:70px;height:3px;background:#f9c9a6;}
.team-title{position:absolute;left:732px;top:2610px;margin:0;font-size:38px;line-height:44px;font-weight:600;color:var(--ink);}

/* news */
.center-label{position:absolute;left:0;width:1200px;text-align:center;}
.news-card{position:absolute;top:3067px;width:322px;height:411px;background:var(--white);box-shadow:0 6px 24px rgba(0,0,0,.07);}
.news-card .thumb{width:322px;height:239px;}
.meta{margin:30px 0 0 31px;font-size:12px;color:#555;}
.news-card h4{margin:14px 0 0 31px;font-size:17px;line-height:25px;font-weight:600;color:var(--ink);}
.more{display:inline-block;margin:18px 0 0 31px;padding:3px 13px;background:#ececec;font-size:11px;font-weight:600;color:#333;}

/* footer */
.footer-col h5{margin:0 0 20px;font-size:17px;font-weight:600;color:var(--white);}
.footer-col{position:absolute;top:3786px;color:var(--white);}
.quick-links{list-style:none;margin:0;padding:0;font-size:12.5px;line-height:31px;}
.contact-row{display:flex;gap:10px;font-size:12.5px;line-height:22px;margin-bottom:17px;}
.contact-row svg{flex:none;margin-top:4px;}
.subscribe{position:absolute;left:850px;top:3885px;width:258px;height:40px;border-radius:20px;background:var(--white);overflow:hidden;}
.subscribe span{position:absolute;left:36px;top:11px;font-size:12px;color:#777;}
.subscribe .send{position:absolute;right:0;top:0;width:40px;height:40px;background:var(--orange);display:flex;align-items:center;justify-content:center;}
.social{position:absolute;top:3950px;width:34px;height:34px;border-radius:50%;background:#2e2e2e;border:1px solid #444;box-sizing:border-box;}
.footer-rule{position:absolute;left:90px;top:4074px;width:1020px;height:1px;background:#333;}
.copyright{position:absolute;left:0;top:4094px;width:1200px;text-align:center;font-size:12.5px;font-weight:600;color:var(--white);letter-spacing:.3px;}
.to-top{position:absolute;left:1130px;top:4049px;width:50px;height:50px;border-radius:50%;background:#2a2a2a;display:flex;align-items:center;justify-content:center;}
</style>
</head>
<body>
<div class="page">

  <!-- hero & about backdrop -->
  <svg class="bg-svg" style="top:0" width="1200" height="1431" viewBox="0 0 748 892" preserveAspectRatio="none">
    <defs>
      <linearGradient id="heroPhoto" x1="0" y1="0" x2="1" y2="1">
        <stop offset="0" stop-color="#d9d4cd"/>
        <stop offset=".5" stop-color="#8c8580"/>
        <stop offset="1" stop-color="#3b3a3c"/>
      </linearGradient>
    </defs>
    <polygon points="0,495 400,370 400,430 0,575" fill="var(--soft)"/>
    <polygon points="0,573 380,456 300,425 400,420 693,300 748,262 748,892 0,892" fill="var(--dark)"/>
    <polygon points="401,63 693,63 693,515 401,420" fill="url(#heroPhoto)" role="img" aria-label="Photo of three consultants reviewing documents and a tablet at a desk"/>
    <g stroke="#6a6a6a" stroke-width="1.2">
      <line x1="187" y1="712" x2="97" y2="625"/>
      <line x1="187" y1="712" x2="261" y2="617"/>
      <line x1="187" y1="712" x2="286" y2="730"/>
      <line x1="286" y1="730" x2="388" y2="760"/>
      <line x1="187" y1="712" x2="96" y2="795"/>
      <line x1="187" y1="712" x2="187" y2="813"/>
    </g>
    <g stroke="#ffffff" stroke-width="2.5">
      <circle cx="97" cy="625" r="30" fill="#c9a28a" role="img" aria-label="Team member portrait"/>
      <circle cx="261" cy="617" r="27" fill="#b7b3ad" role="img" aria-label="Team member portrait"/>
      <circle cx="187" cy="712" r="42" fill="#7d7068" role="img" aria-label="Photo of a team meeting"/>
      <circle cx="286" cy="730" r="30" fill="#8996a6" role="img" aria-label="Photo of colleagues at a laptop"/>
      <circle cx="388" cy="760" r="28" fill="#9a9896" role="img" aria-label="Photo of a consultant on the phone"/>
      <circle cx="96" cy="795" r="34" fill="#a89a7e" role="img" aria-label="Photo of a group workshop"/>
      <circle cx="187" cy="813" r="28" fill="#a9b3bb" role="img" aria-label="Photo of a speaker at an event"/>
    </g>
  </svg>

  <!-- header -->
  <div class="brand">
    <div class="brand-name">Harwell Mariner<br>Advisory LLC</div>
    <div class="brand-mark"></div>
  </div>
  <nav class="nav">
    <span>Home</span><span>About Harwell</span><span>Our Experts</span><span>News and Events</span><span>Careers</span><span>Contact Us</span>
  </nav>

  <!-- hero -->
  <div class="eyebrow" style="left:70px;top:192px;">Optimize IT systems</div>
  <h1 class="hero-title">Fast &amp; effective<br>solutions with<br>Harwell</h1>
  <p class="hero-text">Lorem Ipsum available, but the majority have suffered alteration in some form by injected...</p>
  <div class="btn" style="left:70px;top:514px;width:164px;height:46px;">Get Started</div>

  <!-- about -->
  <h2 class="about-title">About<br>cyber security</h2>
  <p class="about-text" style="top:1064px;">Lorem ipsum dolor etiam rhoncus maecenas tempus, tellus eget condim entum rhon cus sem quam semper libero sit amet adipisc ing sem neque sed ipsum nam quam nunc dolor de sit emit dec lorem.</p>
  <p class="about-text" style="top:1168px;">Entum rhon cus sem quam semper libero sit amet adipisc ing sem neque sed ipsum nam quam nunc dolor de sit emit dec lorem.</p>
  <div class="btn" style="left:723px;top:1266px;width:135px;height:39px;font-size:12px;">Learn More</div>

  <!-- services -->
  <div class="service" style="left:155px;">
    <svg width="90" height="90" viewBox="0 0 90 90" fill="none" stroke="var(--ink)" stroke-width="2">
      <rect x="30" y="6" width="30" height="78" rx="4"/>
      <line x1="40" y1="12" x2="50" y2="12"/>
      <circle cx="45" cy="77" r="2"/>
      <g stroke-width="1.6">
        <rect x="6" y="30" width="7" height="7"/><rect x="16" y="30" width="7" height="7"/><rect x="26" y="30" width="7" height="7"/>
        <rect x="6" y="40" width="7" height="7"/><rect x="16" y="40" width="7" height="7"/>
        <rect x="6" y="50" width="7" height="7"/><rect x="16" y="50" width="7" height="7"/>
      </g>
      <path d="M64 30 a14 14 0 0 1 0 22" stroke="var(--orange)" stroke-width="3"/>
      <circle cx="74" cy="56" r="6" stroke="var(--orange)"/>
    </svg>
    <h3>UI/UX Analysis</h3>
    <p>Lorem Ipsum available, but the majority have suffered...</p>
  </div>
  <div class="service" style="left:448px;">
    <svg width="90" height="90" viewBox="0 0 90 90" fill="none" stroke="var(--ink)" stroke-width="2">
      <rect x="8" y="8" width="56" height="44" rx="2"/>
      <line x1="8" y1="18" x2="64" y2="18"/>
      <line x1="14" y1="13" x2="40" y2="13" stroke="var(--orange)" stroke-width="3"/>
      <line x1="14" y1="26" x2="40" y2="26"/><line x1="14" y1="33" x2="34" y2="33"/>
      <rect x="26" y="38" width="56" height="44" rx="2" fill="var(--white)"/>
      <line x1="26" y1="48" x2="82" y2="48"/>
      <line x1="32" y1="43" x2="58" y2="43" stroke="var(--orange)" stroke-width="3"/>
      <path d="M50 70 l10 -10 M46 66 a5 5 0 0 1 0 -7 l4 -4 a5 5 0 0 1 7 7 M64 62 a5 5 0 0 1 0 7 l-4 4 a5 5 0 0 1 -7 -7"/>
      <path d="M74 6 a10 10 0 0 1 6 12 M74 6 l-3 4"/>
      <path d="M14 84 a10 10 0 0 1 -6 -12 M14 84 l3 -4"/>
    </svg>
    <h3>SEO &amp; Backlinks</h3>
    <p>Lorem Ipsum available, but the majority have suffered...</p>
  </div>
  <div class="service" style="left:742px;">
    <svg width="90" height="90" viewBox="0 0 90 90" fill="none" stroke="var(--ink)" stroke-width="2">
      <circle cx="26" cy="52" r="20"/><circle cx="26" cy="46" r="6"/><path d="M15 66 a11 11 0 0 1 22 0"/>
      <circle cx="62" cy="24" r="14"/><circle cx="62" cy="20" r="4"/><path d="M55 33 a7 7 0 0 1 14 0"/>
      <circle cx="20" cy="18" r="9"/><circle cx="66" cy="66" r="12"/>
      <circle cx="12" cy="12" r="3" stroke="var(--orange)" stroke-width="2.5"/>
      <circle cx="50" cy="52" r="3" stroke="var(--orange)" stroke-width="2.5"/>
      <circle cx="80" cy="44" r="3" stroke="var(--orange)" stroke-width="2.5"/>
      <circle cx="74" cy="80" r="3" stroke="var(--orange)" stroke-width="2.5"/>
    </svg>
    <h3>SMM Production</h3>
    <p>Lorem Ipsum available, but the majority have suffered...</p>
  </div>

  <!-- careers -->
  <div class="photo" role="img" aria-label="Photo of two consultants discussing work at a computer" style="left:523px;top:1777px;width:584px;height:581px;background:linear-gradient(135deg,#3e3a38 0%,#6a5446 45%,#8c5a36 75%,#4a3a30 100%);"></div>
  <div class="abs" style="left:0;top:1854px;width:614px;height:429px;background:var(--white);"></div>
  <svg class="bg-svg" style="top:2283px;left:523px" width="91" height="75" viewBox="0 0 91 75">
    <polygon points="0,0 46,0 91,28 91,75 0,75" fill="var(--dark)"/>
  </svg>
  <div class="eyebrow" style="left:88px;top:1909px;">Our Careers</div>
  <h2 class="careers-title">We are the trusted cyber security experts we keep things simple</h2>
  <p class="careers-text">Lorem ipsum dolor etiam rhoncus maecenas tempus, tellus eget condim entum rhon cus sem quam semper libero sit amet adipisc ing sem neque sed ipsum nam quam nunc dolor de sit emit dec lorem.</p>
  <div class="btn" style="left:92px;top:2215px;width:134px;height:39px;">View Jobs</div>

  <!-- team -->
  <div class="member edge" style="left:-139px;">
    <div class="portrait" role="img" aria-label="Portrait of a team member" style="background:linear-gradient(180deg,#ef9a88,#e07a68);"></div>
    <h4>Michel Havar</h4><span>Manager</span>
  </div>
  <div class="member" style="left:137px;">
    <div class="portrait" role="img" aria-label="Portrait of a project manager" style="background:linear-gradient(180deg,#b9a6cf,#9c86b8);"></div>
    <h4>Idris K. Vane</h4><span>Project Manager</span>
  </div>
  <div class="member active" style="left:413px;">
    <div class="portrait" role="img" aria-label="Portrait of a trainer" style="background:linear-gradient(180deg,#bcd7e8,#9fc2d9);"></div>
    <h4>Nora Castell</h4><span>Gym Trainer</span>
    <div class="view-link">View</div>
  </div>
  <svg class="bg-svg" style="left:618px;top:2843px" width="36" height="36" viewBox="0 0 36 36">
    <circle cx="18" cy="18" r="16" fill="var(--white)" stroke="var(--orange)" stroke-width="3"/>
    <path d="M18 12 v12 M12 18 h12" stroke="var(--ink)" stroke-width="2"/>
  </svg>
  <div class="eyebrow" style="left:733px;top:2584px;">Expert Team</div>
  <h2 class="team-title">Meet our leadership</h2>
  <svg class="bg-svg" style="left:730px;top:2676px" width="140" height="66" viewBox="0 0 140 66" fill="none">
    <circle cx="32" cy="33" r="31" stroke="#cfcfcf" stroke-width="1.5"/>
    <circle cx="106" cy="33" r="31" stroke="#cfcfcf" stroke-width="1.5"/>
    <path d="M42 33 H22 M29 26 l-7 7 7 7" stroke="var(--ink)" stroke-width="2"/>
    <path d="M96 33 H116 M109 26 l7 7 -7 7" stroke="var(--ink)" stroke-width="2"/>
  </svg>

  <!-- news -->
  <div class="center-label" style="top:2979px;font-size:12px;font-weight:600;letter-spacing:.6px;color:#8a8a8a;">ARTICLES</div>
  <h2 class="center-label" style="top:2995px;margin:0;font-size:38px;font-weight:600;color:var(--ink);">News and events</h2>

  <!-- footer backdrop -->
  <svg class="bg-svg" style="top:3368px" width="1200" height="763" viewBox="0 2100 748 476" preserveAspectRatio="none">
    <polygon points="0,2130 440,2258 400,2275 748,2378 748,2576 0,2576" fill="var(--dark)"/>
    <polygon points="275,2210 440,2258 402,2271" fill="var(--orange)"/>
    <polygon points="400,2275 748,2368 748,2386 430,2292" fill="var(--orange)"/>
  </svg>

  <div class="news-card" style="left:90px;">
    <div class="thumb" role="img" aria-label="Photo of a developer working at a laptop" style="background:linear-gradient(135deg,#2c3440,#5a6674 60%,#1e2630);"></div>
    <div class="meta">by Lena &nbsp;-&nbsp; January 2018</div>
    <h4>01: Some blog heading<br>goes right here..</h4>
    <span class="more">MORE</span>
  </div>
  <div class="news-card" style="left:440px;">
    <div class="thumb" role="img" aria-label="Photo of a man studying at a desk" style="background:linear-gradient(135deg,#d8cfc4,#9a7452 55%,#5a4434);"></div>
    <div class="meta">by Lena &nbsp;-&nbsp; January 2018</div>
    <h4>02: Some blog heading<br>goes right here..</h4>
    <span class="more">MORE</span>
  </div>
  <div class="news-card" style="left:788px;">
    <div class="thumb" role="img" aria-label="Photo of hands typing on a laptop" style="background:linear-gradient(135deg,#e6e6e6,#b9b9b9 55%,#8d8d8d);"></div>
    <div class="meta">by Lena &nbsp;-&nbsp; January 2018</div>
    <h4>03: Some blog heading<br>goes right here..</h4>
    <span class="more">MORE</span>
  </div>

  <!-- footer -->
  <div class="brand" style="top:3862px;gap:12px;">
    <div class="brand-name" style="font-size:20px;line-height:24px;letter-spacing:2px;">Harwell Mariner<br>Advisory LLC</div>
    <div class="brand-mark" style="width:16px;height:16px;"></div>
  </div>

  <div class="footer-col" style="left:388px;">
    <h5>Quick Links</h5>
    <ul class="quick-links">
      <li>Home</li><li>About Harwell</li><li>Our Experts</li><li>News and Events</li><li>Careers</li><li>Contact Us</li>
    </ul>
  </div>

  <div class="footer-col" style="left:597px;">
    <h5>Contact info</h5>
    <div class="contact-row">
      <svg width="12" height="10" viewBox="0 0 12 10"><rect width="12" height="10" rx="1" fill="var(--orange)"/><path d="M1 1 l5 4 5 -4" stroke="var(--dark)" fill="none"/></svg>
      <div>Email:<br>hello@harwellmariner.example</div>
    </div>
    <div class="contact-row">
      <svg width="12" height="12" viewBox="0 0 12 12"><path d="M2 1 l3 0 1 3 -2 1 a7 7 0 0 0 3 3 l1 -2 3 1 0 3 a10 10 0 0 1 -9 -9z" fill="var(--orange)"/></svg>
      <div>Phone:<br>555-014-2290</div>
    </div>
    <div class="contact-row">
      <svg width="10" height="14" viewBox="0 0 10 14"><path d="M5 0 a5 5 0 0 1 5 5 c0 4 -5 9 -5 9 s-5 -5 -5 -9 a5 5 0 0 1 5 -5z" fill="var(--orange)"/><circle cx="5" cy="5" r="2" fill="var(--dark)"/></svg>
      <div>Office Location:<br>Some address line goes here</div>
    </div>
  </div>

  <div class="footer-col" style="left:850px;">
    <h5 style="margin-bottom:14px;">Newsletter</h5>
    <div style="font-size:12px;line-height:18px;width:230px;">Subscribe to our email address to get the latest news.</div>
  </div>
  <div class="subscribe">
    <svg class="abs" style="left:16px;top:15px" width="12" height="10" viewBox="0 0 12 10"><rect x=".5" y=".5" width="11" height="9" fill="none" stroke="#aaa"/></svg>
    <span>Enter Your Email...</span>
    <div class="send"><svg width="16" height="16" viewBox="0 0 16 16"><path d="M1 7 L15 1 L10 15 L8 9 Z" fill="var(--white)"/></svg></div>
  </div>
  <div class="social" style="left:852px;" aria-label="Social profile"></div>
  <div class="social" style="left:894px;" aria-label="Social profile"></div>
  <div class="social" style="left:936px;" aria-label="Social profile"></div>

  <div class="footer-rule"></div>
  <div class="to-top"><svg width="16" height="18" viewBox="0 0 16 18"><path d="M8 17 V2 M2 8 L8 2 L14 8" stroke="var(--white)" stroke-width="1.6" fill="none"/></svg></div>
  <div class="copyright">COPYRIGHT 2020 © HARWELL MARINER. ALL RIGHT RESERVED</div>

</div>
</body>
</html>
```